The Copper Fellow Mo Wax Label

Hi Chaps,

We are needing a lable for our new moustache wax.

The design needs to be on a circular label. the size of the label is 32mm in diameter.

It needs to align with our branding from our beard oil product. checkout www.thecopperfellow-demo.com to get an insight of this.

what needs to be on the label:

- The copper fellow logo (please pull from website, will send through hi def image when design is selected)
- Fine Grain Moustache Wax
- the word "soft/medium hold"

This project will be open for 48 hours.

Any questions, please ask asap.
Updates

Our Logo and fonts that we use for our brand are now attached to the brief. 

Industry/Entity Type

Product

Requirements
Must have
• Must have
The copper fellow logo (please pull from website, will send through hi def image when design is selected)
- Fine Grain Moustache Wax
- allign with branding
- actual size 32mm diameter

```html
<!DOCTYPE html>
<html lang="en">
<head>
<meta charset="utf-8">
<title>The Copper Fellow – Fine Grain Moustache Wax Labels</title>
<link rel="stylesheet" href="https://fonts.googleapis.com/css2?family=Alfa+Slab+One&family=PT+Sans:wght@400;700&display=swap">
<style>
  :root {
    --backdrop: #a3a3a3;
    --label-cream: #eeede5;
    --ink: #1c1b19;
    --rule-brown: #6b5442;
    --flourish-tone: #d6d4c8;
    --hold-soft: #8c2a36;
    --hold-hard: #2f3b70;
  }
  html, body {
    margin: 0;
    width: 1200px;
    height: 593px;
    overflow: hidden;
    background: var(--backdrop);
  }
  .label-sheet {
    position: relative;
    width: 1200px;
    height: 593px;
  }
  .wax-label {
    position: absolute;
    top: 40px;
    width: 512px;
    height: 512px;
  }
  .wax-label--soft { left: 74px; }
  .wax-label--hard { left: 624px; }
  .wax-label svg { display: block; width: 512px; height: 512px; }
  .label-face { fill: var(--label-cream); }
  .dot-ring { fill: none; stroke: var(--rule-brown); stroke-width: 3; stroke-linecap: round; stroke-dasharray: 0 7; }
  .dot-row { fill: none; stroke: var(--rule-brown); stroke-width: 2.6; stroke-linecap: round; stroke-dasharray: 0 5.5; }
  .dot-bar { stroke: var(--ink); stroke-width: 1.6; }
  .hold-rule { stroke: var(--rule-brown); stroke-width: 1.2; }
  .flourish-area { fill: var(--flourish-tone); }
  .brand-name {
    font-family: "Alfa Slab One", serif;
    fill: var(--ink);
    text-anchor: middle;
    font-size: 40px;
  }
  .range-word, .product-name {
    font-family: "Alfa Slab One", serif;
    fill: var(--ink);
    font-variant: small-caps;
  }
  .range-word { font-size: 26px; text-anchor: middle; }
  .product-name { font-size: 44px; text-anchor: middle; }
  .hold-text {
    font-family: "PT Sans", sans-serif;
    font-size: 21px;
    text-anchor: middle;
  }
  .wax-label--soft .hold-text { fill: var(--hold-soft); }
  .wax-label--hard .hold-text { fill: var(--hold-hard); }
  .web-address {
    font-family: "PT Sans", sans-serif;
    font-weight: 700;
    font-size: 17px;
    fill: var(--ink);
    text-anchor: middle;
    font-variant: small-caps;
    letter-spacing: 0.5px;
  }
</style>
</head>
<body>
<main class="label-sheet">

  <section class="wax-label wax-label--soft">
    <svg viewBox="0 0 512 512">
      <circle class="label-face" cx="256" cy="256" r="256"/>
      <circle class="dot-ring" cx="256" cy="256" r="245"/>
      <rect class="flourish-area" x="78" y="105" width="62" height="150" rx="24" role="img" aria-label="Decorative scroll flourish"/>
      <rect class="flourish-area" x="372" y="105" width="62" height="150" rx="24" role="img" aria-label="Decorative scroll flourish"/>
      <text class="brand-name" x="256" y="180">The Copper</text>
      <text class="brand-name" x="256" y="228">Fellow</text>
      <line class="dot-row" x1="82" y1="290" x2="140" y2="290"/>
      <line class="dot-row" x1="372" y1="290" x2="432" y2="290"/>
      <text class="range-word" x="110" y="322">Fine</text>
      <text class="range-word" x="400" y="322">Grain</text>
      <text class="product-name" x="256" y="366" textLength="350" lengthAdjust="spacingAndGlyphs">Moustache Wax</text>
      <line class="dot-row" x1="128" y1="384" x2="385" y2="384"/>
      <line class="hold-rule" x1="128" y1="392" x2="385" y2="392"/>
      <line class="hold-rule" x1="128" y1="424" x2="385" y2="424"/>
      <g class="dot-bar">
        <line x1="92" y1="400" x2="92" y2="416"/><line x1="98" y1="400" x2="98" y2="416"/><line x1="104" y1="400" x2="104" y2="416"/><line x1="110" y1="400" x2="110" y2="416"/><line x1="116" y1="400" x2="116" y2="416"/>
        <line x1="396" y1="400" x2="396" y2="416"/><line x1="402" y1="400" x2="402" y2="416"/><line x1="408" y1="400" x2="408" y2="416"/><line x1="414" y1="400" x2="414" y2="416"/><line x1="420" y1="400" x2="420" y2="416"/>
      </g>
      <text class="hold-text" x="256" y="416">SOFT/MEDIUM HOLD</text>
      <text class="web-address" x="256" y="460">TheCopperFellow-demo.com</text>
    </svg>
  </section>

  <section class="wax-label wax-label--hard">
    <svg viewBox="0 0 512 512">
      <circle class="label-face" cx="256" cy="256" r="256"/>
      <circle class="dot-ring" cx="256" cy="256" r="245"/>
      <rect class="flourish-area" x="78" y="105" width="62" height="150" rx="24" role="img" aria-label="Decorative scroll flourish"/>
      <rect class="flourish-area" x="372" y="105" width="62" height="150" rx="24" role="img" aria-label="Decorative scroll flourish"/>
      <text class="brand-name" x="256" y="180">The Copper</text>
      <text class="brand-name" x="256" y="228">Fellow</text>
      <line class="dot-row" x1="82" y1="290" x2="140" y2="290"/>
      <line class="dot-row" x1="372" y1="290" x2="432" y2="290"/>
      <text class="range-word" x="110" y="322">Fine</text>
      <text class="range-word" x="400" y="322">Grain</text>
      <text class="product-name" x="256" y="366" textLength="350" lengthAdjust="spacingAndGlyphs">Moustache Wax</text>
      <line class="dot-row" x1="128" y1="384" x2="385" y2="384"/>
      <line class="hold-rule" x1="128" y1="392" x2="385" y2="392"/>
      <line class="hold-rule" x1="128" y1="424" x2="385" y2="424"/>
      <g class="dot-bar">
        <line x1="92" y1="400" x2="92" y2="416"/><line x1="98" y1="400" x2="98" y2="416"/><line x1="104" y1="400" x2="104" y2="416"/><line x1="110" y1="400" x2="110" y2="416"/><line x1="116" y1="400" x2="116" y2="416"/>
        <line x1="396" y1="400" x2="396" y2="416"/><line x1="402" y1="400" x2="402" y2="416"/><line x1="408" y1="400" x2="408" y2="416"/><line x1="414" y1="400" x2="414" y2="416"/><line x1="420" y1="400" x2="420" y2="416"/>
      </g>
      <text class="hold-text" x="256" y="416">HARD/STRONG HOLD</text>
      <text class="web-address" x="256" y="460">TheCopperFellow-demo.com</text>
    </svg>
  </section>

</main>
</body>
</html>
```